Talvo shoes is a wholesale shoe sales company , mostly working in female shoes and kiddies shoes with a small mens section . looking for a clean slick look. http://www.kemrafootwear.co.za/shop/ is a good reference

It Company

```html
<!DOCTYPE html>
<html lang="en">
<head>
<meta charset="utf-8">
<title>Talvo Shoes – Home</title>
<link rel="stylesheet" href="https://fonts.googleapis.com/css2?family=Questrial&family=Montserrat:wght@600&display=swap">
<style>
  :root {
    --orange: #f7941d;
    --text: #7a7a7a;
    --text-dark: #555555;
    --rule: #d9d9d9;
    --band: #eeeeee;
    --page: #ffffff;
  }
  * { margin: 0; padding: 0; box-sizing: border-box; }
  html, body { width: 839px; height: 1200px; overflow: hidden; background: var(--page); }
  body { position: relative; font-family: "Questrial", sans-serif; color: var(--text); }

  .brand { position: absolute; left: 38px; top: 16px; font-family: "Montserrat", sans-serif; font-weight: 600; font-size: 40px; color: var(--orange); letter-spacing: 1px; }

  .languages { position: absolute; left: 590px; top: 16px; display: flex; gap: 6px; }
  .languages span { width: 14px; height: 9px; background: #c9c9d2; border: 1px solid #b5b5c0; }
  .account-links { position: absolute; left: 560px; top: 40px; display: flex; gap: 18px; font-size: 8px; color: var(--text); }

  .main-nav { position: absolute; left: 336px; top: 104px; display: flex; gap: 25px; font-size: 13px; color: var(--text); }
  .main-nav .active, .footer-nav .active { color: var(--orange); }
  .nav-rule { position: absolute; left: 280px; top: 131px; width: 480px; height: 1px; background: var(--rule); }

  .hero { position: absolute; left: 0; top: 140px; width: 839px; height: 330px; background: linear-gradient(180deg, #ffffff 0%, #f3f3f3 75%, #ffffff 100%); }
  .hero-title { position: absolute; left: 112px; top: 182px; font-size: 20px; line-height: 22px; color: var(--orange); text-transform: uppercase; letter-spacing: 0.5px; }
  .hero-photo { position: absolute; left: 212px; top: 172px; width: 335px; height: 220px; background: linear-gradient(135deg, #8a6a4a 0%, #c7a27a 45%, #e8d2b8 70%, #6d5a48 100%); }
  .hero-arrow { position: absolute; top: 272px; }
  .hero-arrow.prev { left: 188px; }
  .hero-arrow.next { left: 566px; }
  .hero-dots { position: absolute; left: 360px; top: 440px; display: flex; gap: 8px; }
  .hero-dots span { width: 5px; height: 5px; border-radius: 50%; background: #9a9a9a; }
  .hero-dots span.current { background: var(--orange); }

  .product-strip { position: absolute; left: 0; top: 488px; width: 839px; height: 92px; background: linear-gradient(180deg, #f7f7f7, #ececec); }
  .strip-arrow { position: absolute; top: 510px; }
  .strip-arrow.prev { left: 6px; }
  .strip-arrow.next { left: 818px; }
  .product-thumbs { position: absolute; left: 40px; top: 494px; display: flex; gap: 22px; }
  .product-thumb { width: 127px; height: 80px; border-right: 1px solid var(--rule); }
  .product-thumb:last-child { border-right: none; }

  h2 { font-weight: 400; font-size: 18px; color: var(--text); }
  .about { position: absolute; left: 112px; top: 652px; width: 180px; }
  .about h2 { margin-bottom: 6px; }
  .about p { font-size: 9.5px; line-height: 13px; margin-bottom: 10px; }
  .about h2.second { margin-top: 22px; }
  .column-divider { position: absolute; left: 308px; top: 655px; width: 1px; height: 450px; background: var(--rule); }

  .news { position: absolute; left: 341px; top: 652px; width: 395px; }
  .news h2 { margin-bottom: 10px; }
  .news-item { border-bottom: 1px solid var(--rule); padding-bottom: 6px; margin-bottom: 8px; }
  .news-date { font-size: 11px; color: var(--text-dark); font-weight: 700; }
  .news-title { font-size: 11px; color: var(--orange); margin-left: 72px; margin-top: -14px; }
  .news-body { font-size: 9.5px; line-height: 12px; margin-left: 72px; color: var(--text); }
  .news-photo { width: 392px; height: 232px; margin: 10px 0 12px; background: linear-gradient(160deg, #7d6a4a 0%, #b99c6e 40%, #e6dcc9 65%, #8f7552 100%); }
  .news-more { position: absolute; left: 690px; top: 1098px; }

  .footer-rule { position: absolute; left: 40px; top: 1125px; width: 760px; height: 1px; background: var(--rule); }
  .footer-nav { position: absolute; left: 228px; top: 1139px; width: 400px; display: flex; justify-content: center; gap: 22px; font-size: 11px; }
  .copyright { position: absolute; left: 0; top: 1162px; width: 839px; text-align: center; font-size: 8px; }
</style>
</head>
<body>
  <header>
    <div class="brand">TALVO</div>
    <div class="languages" aria-label="Language selection"><span></span><span></span><span></span><span></span><span></span></div>
    <div class="account-links"><span>My account</span><span>My Orders</span><span>My Wishlist</span></div>
    <nav class="main-nav">
      <span class="active">Home</span><span>About Us</span><span>Talvo Store</span><span>Talvo Events</span><span>News</span><span>Contact</span>
    </nav>
    <div class="nav-rule"></div>
  </header>

  <section>
    <div class="hero"></div>
    <div class="hero-title">Woman<br>Shoes</div>
    <div class="hero-photo" role="img" aria-label="Photo of a woman's legs in high-heeled sandals"></div>
    <svg class="hero-arrow prev" width="10" height="16" viewBox="0 0 10 16"><polyline points="8,1 2,8 8,15" fill="none" stroke="#666" stroke-width="1.5"/></svg>
    <svg class="hero-arrow next" width="10" height="16" viewBox="0 0 10 16"><polyline points="2,1 8,8 2,15" fill="none" stroke="#666" stroke-width="1.5"/></svg>
    <div class="hero-dots"><span></span><span></span><span></span><span class="current"></span><span></span><span></span><span></span></div>
  </section>

  <section>
    <div class="product-strip"></div>
    <svg class="strip-arrow prev" width="12" height="40" viewBox="0 0 12 40"><polyline points="10,2 2,20 10,38" fill="none" stroke="#888" stroke-width="1.5"/></svg>
    <svg class="strip-arrow next" width="12" height="40" viewBox="0 0 12 40"><polyline points="2,2 10,20 2,38" fill="none" stroke="#888" stroke-width="1.5"/></svg>
    <div class="product-thumbs">
      <div class="product-thumb" role="img" aria-label="Pink high-heeled shoe" style="background:radial-gradient(ellipse at center,#e9a6a0 0%,#f2d6d2 45%,#f6f6f6 75%)"></div>
      <div class="product-thumb" role="img" aria-label="Black peep-toe heel" style="background:radial-gradient(ellipse at center,#3a3a3a 0%,#9a9a9a 45%,#f6f6f6 75%)"></div>
      <div class="product-thumb" role="img" aria-label="Woman wearing heels" style="background:linear-gradient(135deg,#7a5a3a,#c9a77f,#5a4a3a)"></div>
      <div class="product-thumb" role="img" aria-label="Black leather pump" style="background:radial-gradient(ellipse at center,#2e2e2e 0%,#8e8e8e 45%,#f6f6f6 75%)"></div>
      <div class="product-thumb" role="img" aria-label="Red-soled stiletto" style="background:radial-gradient(ellipse at center,#c84c3c 0%,#e6b7a8 45%,#f6f6f6 75%)"></div>
    </div>
  </section>

  <section class="about">
    <h2>Who we are?</h2>
    <p>Lorem ipsum dolor sit amet, consectetuer adipiscing elit. Aenean commodo ligula eget dolor. Aenean massa. Cum sociis natoque penatibus et magnis dis parturient montes.</p>
    <p>Nullam dictum felis eu pede mollis pretium. Integer tincidunt. Cras dapibus. Vivamus elementum semper nisi. Aenean vulputate eleifend tellus. Aenean leo ligula, porttitor eu, consequat vitae.</p>
    <p>Phasellus viverra nulla ut metus varius laoreet. Quisque rutrum. Aenean imperdiet. Etiam ultricies nisi vel augue.</p>
    <h2 class="second">What do we?</h2>
    <p>Donec quam felis, ultricies nec, pellentesque eu, pretium quis, sem. Nulla consequat massa quis enim. Donec pede justo, fringilla vel, aliquet nec, vulputate eget, arcu.</p>
  </section>
  <div class="column-divider"></div>

  <section class="news">
    <h2>Latest News</h2>
    <article class="news-item">
      <div class="news-date">(5/19/2014)</div>
      <div class="news-title">Lorem ipsum dolor sit amet</div>
      <div class="news-body">Lorem ipsum dolor sit amet, consectetuer adipiscing elit. Aenean commodo ligula eget dolor. Aenean massa.</div>
      <div class="news-photo" role="img" aria-label="Woman in a white dress seated on a sofa with rows of shoes on the floor"></div>
    </article>
    <article class="news-item">
      <div class="news-date">(5/17/2014)</div>
      <div class="news-title">Lorem ipsum dolor sit amet</div>
      <div class="news-body">Lorem ipsum dolor sit amet, consectetuer adipiscing elit. Aenean commodo ligula eget dolor. Aenean massa.</div>
    </article>
    <article class="news-item">
      <div class="news-date">(5/16/2013)</div>
      <div class="news-title">Lorem ipsum dolor sit amet</div>
      <div class="news-body">Lorem ipsum dolor sit amet, consectetuer adipiscing elit. Aenean commodo ligula eget dolor. Aenean massa.</div>
    </article>
  </section>
  <svg class="news-more" width="44" height="10" viewBox="0 0 44 10"><polyline points="1,1 22,9 43,1" fill="none" stroke="#888" stroke-width="1.2"/></svg>

  <footer>
    <div class="footer-rule"></div>
    <nav class="footer-nav">
      <span class="active">Home</span><span>About Us</span><span>Talvo Store</span><span>Talvo Events</span><span>News</span><span>Contact</span>
    </nav>
    <div class="copyright">© 2014 Talvo Shoes. All Rights Reserved.</div>
  </footer>
</body>
</html>
```